Im looking to drive the very foundation of our business into a differnet direction. With a team of

We need to develop firstly a corporate profile that really gets the attentions of the reader. From here I want then to develop a report format (template) that we can overlay the reports we do. We have a logo and tat that can be found at www.brindlewoodgroup.com.au. I want to stay with the lime green and blue to be sure we stay on the same branding message we already have.

The final design should communicate as the business is named Corvane Ridge Tallmark Partners Australia.

Download Purchased Pixelmoor image here:
https://www.filequarry.net/s/k27vbq81ntaxzre/pixelmoor_504918263.jpg?dl=0

Target Market(s)

Large corporate clents

Industry/Entity Type

Consulting

Requirements
Must have
• Photos not animated pictures

```html
<!DOCTYPE html>
<html lang="en">
<head>
<meta charset="utf-8">
<title>Corvane Ridge Tallmark Partners Australia – Corporate Profile</title>
<link rel="stylesheet" href="https://fonts.googleapis.com/css2?family=Source+Serif+4:wght@400;600;700&display=swap">
<style>
  :root{
    --lime:#8cc63f;
    --lime-dark:#6fa52a;
    --navy:#1f3f6e;
    --body:#44607f;
    --paper:#ffffff;
    --sky:#cfe0ee;
  }
  *{margin:0;padding:0;box-sizing:border-box}
  html,body{width:849px;height:1200px;overflow:hidden;background:var(--paper)}
  .profile{position:relative;width:849px;height:1200px;background:var(--paper);
    font-family:"Source Serif 4",Georgia,serif;color:var(--body);font-size:14.6px;line-height:19px}
  .hero{position:absolute;left:0;top:0;width:849px;height:300px;
    background:linear-gradient(180deg,#b9d2e6 0%,#dbe7f1 55%,#ffffff 100%),
               linear-gradient(90deg,#e8eef4 0%,#c7d9ea 100%)}
  .hero::after{content:"";position:absolute;right:60px;top:0;width:330px;height:280px;
    background:radial-gradient(ellipse at 55% 40%,rgba(140,160,185,.55),rgba(255,255,255,0) 70%)}
  .brand{position:absolute;left:42px;top:190px;display:flex;align-items:center;gap:12px}
  .brand-dot{width:44px;height:44px;border-radius:50%;background:var(--lime)}
  .brand-name{font-size:25px;font-weight:700;color:var(--navy);line-height:1.1}
  .content{position:absolute;left:42px;top:252px;width:765px}
  .content p{margin-bottom:9px}
  .lead-heading{font-size:19px;font-weight:700;color:var(--navy);margin:6px 0 3px}
  .section-title{font-size:25px;font-weight:700;color:var(--lime-dark);margin:8px 0 4px}
  .list{list-style:none;margin:0 0 8px 18px}
  .list li{position:relative;padding-left:18px;color:var(--navy)}
  .list li::before{content:"›";position:absolute;left:0;top:-1px;color:var(--lime);font-weight:700;font-size:17px}
  .footer-band{position:absolute;left:0;bottom:0;width:849px;height:78px;
    background:linear-gradient(180deg,#ffffff 0%,#cfe6ab 40%,var(--lime) 100%)}
</style>
</head>
<body>
<main class="profile">
  <div class="hero" role="img" aria-label="Photograph of a smiling safety consultant in a yellow hard hat and high-visibility vest"></div>

  <div class="brand">
    <span class="brand-dot"></span>
    <span class="brand-name">Corvane Ridge Tallmark Partners Australia</span>
  </div>

  <section class="content">
    <p>Our partnership approach with clients and unique blend of experience and expertise continues to be the very essence of our success. Our marketing approach is simply, our reputation, across industry, resources, government and defence.</p>
    <p>Our team of well qualified scientific and technical experts provide a practical and “fit for purpose” project focus suited for effective, accurate and informed decision-making. We really have a unique value proposition, simply, a single source for a diverse range of health, safety and environmental risk analysis and assessment services.</p>
    <p>Partnering with Halvern Minerals for us to be so successful, that Corvane Ridge were awarded “The Best Solution To an Identified Workplace Health &amp; Safety Issue” at the recent 2010 Southern Workplace Safety Awards. As partners in safety, we listened to our client and developed an engineering solution to identify asbestos fibres in soil, in drilling samples.</p>

    <h2 class="lead-heading">Our key areas of success surround:</h2>
    <ul class="list">
      <li>Occupational Health and Safety</li>
      <li>Occupational Hygiene</li>
      <li>Environmental Solutions</li>
      <li>Laboratory Services Analysis - QLAB Accredited</li>
      <li>Property Services Training</li>
    </ul>

    <h2 class="section-title">Occupational Health and Safety</h2>
    <p>Corvane Ridge Tallmark Partners Australia are industry experts, providing consulting services surrounding OH&amp;S strategy planning and implementation across a business, right through to independent incident investigation. Our team are working with clients, building links and planning the implementation that will support businesses to meet the prescribed national Harmonisation legislation changes due early 2012. This is being implemented through the provision of appropriate OHS systems and training and also conducting internal and external OHS management systems audits.</p>

    <h2 class="lead-heading">The range of services includes:</h2>
    <ul class="list">
      <li>OHS Management Systems Analysis, Development and Implementation.</li>
      <li>Third party independent Auditing in OHS compliance</li>
      <li>Strategic Management</li>
      <li>Business Planning</li>
      <li>Leadership and Team Building</li>
      <li>Management of Contractors</li>
      <li>Independent Incident/Accident investigations</li>
      <li>Independent risk assessments</li>
      <li>OHS team leadership and facilitation workshops</li>
    </ul>
  </section>

  <div class="footer-band"></div>
</main>
</body>
</html>
```